Kestrel Ridgeway LLC stationery, business card and web page design.

i need a full set of stationery designed using the name "Kestrel Ridgeway LLC" with a tag line "construction consulting services". using the uploaded monkey icon as the logo.

i like the colors orange, green and black in general but im not limited to that. the company offers consulting services to various types of construction businesses.

Target Market(s)

i travel around the country in a 4x4 camper offering consulting services and technical training short term and long to various types of construction companies.

Industry/Entity Type

Construction Company

Contact Information for Business Card

Martin Hale
m.hale@kestrelridgeway.example
2475 Birchfield Rd
Bohemia, NY 11716
555 314 0627

list these services on the card.

Business Consulting
Capital Investments
Marketing Implementations
Technical Training

Number of Pages Required

1 page

Colors

Designer to choose colors to be used in the design.

Requirements
Must have
• company info and use of the monkey icon i provided.
Nice to have
• a fun but professional design
Should not have
• the color red

```html
<!DOCTYPE html>
<html lang="en">
<head>
<meta charset="utf-8">
<title>Kestrel Ridgeway LLC – Business Card</title>
<link rel="stylesheet" href="https://fonts.googleapis.com/css2?family=Quicksand:wght@400;500;600&display=swap">
<style>
  :root {
    --stage: #3a3a3c;
    --card: #ffffff;
    --orange: #f0612b;
    --green: #8cc43f;
    --slate: #58585a;
    --charcoal: #3b3b3d;
    --ink: #1a1a1a;
    --muted: #8a8a8a;
    --text: #505050;
    --ghost: #f2f2f2;
  }
  * { margin: 0; padding: 0; box-sizing: border-box; }
  html, body {
    width: 1200px; height: 575px; overflow: hidden;
    background: var(--stage);
    font-family: "Quicksand", sans-serif;
  }
  .stage { position: relative; width: 1200px; height: 575px; }

  .card {
    position: absolute;
    width: 446px; height: 254px;
    background: var(--card);
    border-radius: 13px;
    overflow: hidden;
    box-shadow: 4px 5px 8px rgba(0,0,0,0.45);
  }
  .card--front { left: 98px; top: 138px; }
  .card--back  { left: 577px; top: 139px; }

  .waves { position: absolute; inset: 0; width: 446px; height: 254px; }

  .brand-mark {
    position: absolute; left: 72px; top: 18px;
    width: 56px; height: 56px; border-radius: 50%;
    background: var(--ink);
  }
  .brand-name {
    position: absolute; left: 147px; top: 30px;
    font-size: 21px; font-weight: 500; color: var(--orange);
    letter-spacing: 0.5px; white-space: nowrap;
  }
  .brand-tagline {
    position: absolute; left: 147px; top: 61px;
    font-size: 9.5px; font-weight: 500; color: var(--muted);
    letter-spacing: 1px; white-space: nowrap;
  }
  .person {
    position: absolute; left: 0; right: 0; top: 104px;
    text-align: center; color: var(--text); white-space: nowrap;
  }
  .person__name { font-size: 19px; font-weight: 400; }
  .person__role { font-size: 14px; font-weight: 500; }

  .contact {
    position: absolute; left: 0; right: 0; top: 190px;
    text-align: center; color: #ffffff;
  }
  .contact__line { font-size: 10px; font-weight: 500; letter-spacing: 0.4px; line-height: 14px; }
  .contact__web { font-size: 12px; font-weight: 600; letter-spacing: 0.6px; margin-top: 6px; }

  .back-mark {
    position: absolute; left: 101px; top: 10px;
    width: 232px; height: 232px; border-radius: 50%;
    background: var(--ghost);
  }
  .web-pill {
    position: absolute; left: 78px; top: 175px;
    width: 283px; height: 25px; border-radius: 13px;
    background: var(--orange); color: #ffffff;
    font-size: 14px; font-weight: 600; letter-spacing: 2.2px;
    display: flex; align-items: center; justify-content: center;
    white-space: nowrap;
  }
</style>
</head>
<body>
<main class="stage">
  <section class="card card--front">
    <svg class="waves" viewBox="0 0 446 254" aria-hidden="true">
      <path d="M0,66 C110,160 290,190 446,105 V254 H0 Z" fill="var(--slate)"/>
      <path d="M0,100 C130,178 300,180 446,53 V254 H0 Z" fill="var(--green)"/>
      <path d="M0,106 C135,184 300,188 446,71 V254 H0 Z" fill="var(--charcoal)"/>
      <path d="M0,109 C140,190 300,192 446,86 V254 H0 Z" fill="var(--orange)"/>
    </svg>
    <div class="brand-mark"></div>
    <div class="brand-name">Kestrel Ridgeway LLC</div>
    <div class="brand-tagline">CONSTRUCTION CONSULTING SERVICES</div>
    <div class="person"><span class="person__name">Your Name,</span> <span class="person__role">Director</span></div>
    <div class="contact">
      <p class="contact__line">Suite 123, City name,&nbsp;&nbsp; CountryName 12345</p>
      <p class="contact__line">012.345.6789, info@kestrelridgeway.example</p>
      <p class="contact__web">www.KestrelRidgewayllc.example</p>
    </div>
  </section>

  <section class="card card--back">
    <div class="back-mark"></div>
    <div class="web-pill">www.KestrelRidgeway.example</div>
  </section>
</main>
</body>
</html>
```